I dont have a logo yet. My mind in color is navy blue and khaki maybe a tiny bit of yellow but open to ideas. name of the business is Granite Ridge Builders. Dedicated to all sorts of construction commerical and residential. Im Tomas Vantrell owner of business<br/>Address to business is 862 N. Berrymoor El Paso Tx 79931 <br/>Phone is 9155827143<br/>Id like round corners i also like the see thru card a little.<br/>Open to trademark quotes

Target Market(s)

Construction

Contact Information for Business Card

GRANITE RIDGE BUILDERS LLC

Tomas Vantrell
Director of Operations

Commercial & Residential

9155827143
GRANITE.R.BUILDERS@QUORVANMAIL.COM

Colors
0355a3
fff3d1

Requirements
Must have
• ROUND CORNERS
• BLUE AND KHAKI AND CLEAR
• LOGO

```html
<!DOCTYPE html>
<html lang="en">
<head>
<meta charset="utf-8">
<title>Granite Ridge Builders – Business Card</title>
<link href="https://fonts.googleapis.com/css2?family=Montserrat:wght@400;600;700&display=swap" rel="stylesheet">
<style>
  :root {
    --backdrop: #d8d1c7;
    --navy-deep: #0a1560;
    --navy-soft: #34479a;
    --khaki: #b07d4f;
    --khaki-light: #c9a27a;
    --cream: #f3ead8;
    --ink: #141a4a;
    --frost-1: #e9ecef;
    --frost-2: #c9c3b8;
  }
  * { margin: 0; padding: 0; box-sizing: border-box; }
  html, body {
    width: 1200px; height: 1098px; overflow: hidden;
    background: var(--backdrop);
    font-family: "Montserrat", sans-serif;
  }
  .card {
    position: absolute; left: 80px; top: 253px;
    width: 1040px; height: 592px;
    border-radius: 18px; overflow: hidden;
    box-shadow: 0 18px 40px rgba(40, 30, 20, .25);
  }
  .card-art { position: absolute; inset: 0; width: 100%; height: 100%; }
  .text { position: absolute; white-space: nowrap; line-height: 1; }
  .person-name {
    left: 55px; top: 126px; font-size: 42px; font-weight: 600;
    color: var(--khaki-light);
  }
  .person-title { left: 55px; top: 174px; font-size: 31px; color: var(--cream); }
  .service { left: 55px; font-size: 27px; color: var(--cream); }
  .service-1 { top: 252px; }
  .service-2 { top: 288px; }
  .address { left: 55px; font-size: 27px; color: var(--cream); }
  .address-1 { top: 370px; }
  .address-2 { top: 416px; }
  .contact { left: 55px; font-size: 27px; color: var(--cream); display: flex; align-items: center; }
  .contact-phone { top: 463px; }
  .contact-email { top: 510px; }
  .contact svg { width: 28px; height: 30px; margin-right: 25px; }
  .company {
    position: absolute; left: 580px; width: 460px; top: 285px;
    text-align: center; color: var(--ink);
    font-size: 29px; font-weight: 700; line-height: 1.15;
  }
  .company-mark {
    display: block; width: 70px; height: 70px; margin: 0 auto 36px;
    background: var(--ink);
  }
</style>
</head>
<body>
  <div class="card">
    <svg class="card-art" viewBox="0 0 1180 672" preserveAspectRatio="none" aria-hidden="true">
      <defs>
        <linearGradient id="navy" x1="0" y1="0" x2="1" y2="0.3">
          <stop offset="0" stop-color="#3a4d9e"/>
          <stop offset="0.35" stop-color="#263a94"/>
          <stop offset="0.7" stop-color="#0a1560"/>
          <stop offset="1" stop-color="#0a1358"/>
        </linearGradient>
        <linearGradient id="frost" x1="0" y1="0" x2="0.6" y2="1">
          <stop offset="0" stop-color="#f2f4f6"/>
          <stop offset="0.5" stop-color="#dfdcd6"/>
          <stop offset="1" stop-color="#c7bdb0"/>
        </linearGradient>
        <linearGradient id="khaki" x1="0" y1="0" x2="1" y2="1">
          <stop offset="0" stop-color="#b3814f"/>
          <stop offset="1" stop-color="#9a6b43"/>
        </linearGradient>
      </defs>
      <rect width="1180" height="672" fill="url(#frost)"/>
      <polygon points="0,0 895,0 615,165 615,505 895,672 0,672" fill="url(#navy)"/>
      <polygon points="895,0 990,0 660,190 660,480 990,672 895,672 615,505 615,165" fill="url(#khaki)"/>
    </svg>

    <div class="text person-name">Tomas Vantrell</div>
    <div class="text person-title">Directo of operations</div>
    <div class="text service service-1">Commercial &amp;</div>
    <div class="text service service-2">Residential construction</div>
    <div class="text address address-1">862 N. Berrymoor</div>
    <div class="text address address-2">El Paso Tx 79931</div>
    <div class="text contact contact-phone">
      <svg viewBox="0 0 28 30" aria-hidden="true"><rect x="6" y="1" width="15" height="28" rx="3" fill="none" stroke="#c9a27a" stroke-width="2"/><line x1="12" y1="25" x2="15" y2="25" stroke="#c9a27a" stroke-width="2"/></svg>
      915-582-7143
    </div>
    <div class="text contact contact-email">
      <svg viewBox="0 0 28 30" aria-hidden="true"><rect x="1" y="7" width="26" height="17" fill="#c9a27a"/><polyline points="1,7 14,17 27,7" fill="none" stroke="#34479a" stroke-width="2"/></svg>
      granite.r.builders@quorvanmail.com
    </div>

    <div class="company">
      <span class="company-mark"></span>
      GRANITE RIDGE<br>BUILDERS LLC
    </div>
  </div>
</body>
</html>
```